Chiropractic office needs updated web site

take the information/content from my existing website and redesign it to be more efficient and modern looking. i have a logo already designed that i have provided the files for. my office sees primarily athletes and their families and is geared toward active, healthy people who have sports injuries.
Updates

i originally started the project in february 2019 but am now just able to post the project. i need a new deadline calculated from todays (6-9-19) date.

Target Market(s)

injured athletes looking for a specific type of chiropractor.

Industry/Entity Type

Health Care

Contact Information for Business Card

I have a logo already designed and will provide that to all designers!

Coding

Coded - Design and coding required

Number of Pages Required

1 page

Font styles to use
Sans Serif

Colors

Designer to choose colors to be used in the design.

Requirements
Must have
• the current information/content already contained in my current website, belvanspinefit.com. i want this info redesigned and/or transferred to a new template. i will also provide new updated photos for use on the new site!
Nice to have
• modern, minimalist, creative looking website
Should not have
• typical medical website with boring, over-used stock photos of doctors, nurses and generic family types

```html
<!DOCTYPE html>
<html lang="en">
<head>
<meta charset="utf-8">
<title>Belvan Chiropractic and Sports Therapy</title>
<link rel="stylesheet" href="https://fonts.googleapis.com/css2?family=Poppins:ital,wght@0,300;0,400;0,500;0,600;1,300&family=Questrial&display=swap">
<style>
:root{
  --cyan:#00bff3;
  --red:#e8192c;
  --ink:#1f1f1f;
  --body:#5a5a5a;
  --dark:#262626;
  --darker:#1b1b1b;
  --white:#ffffff;
  --line:#e3e3e3;
}
*{box-sizing:border-box;margin:0;padding:0}
html,body{width:1200px;height:5013px;overflow:hidden;background:var(--white)}
body{position:relative;font-family:"Poppins",sans-serif;color:var(--body)}
.abs{position:absolute}
a{color:inherit;text-decoration:none}

/* header */
.brand{display:flex;align-items:center;gap:12px}
.brand-dot{width:54px;height:54px;border-radius:50%;background:var(--cyan);flex:none}
.brand-name{font-family:"Poppins",sans-serif;font-weight:500;color:var(--cyan);font-size:19px;line-height:1.15;letter-spacing:2px;text-transform:uppercase}
.header-phone{left:706px;top:32px;font-size:16px;color:var(--ink);display:flex;align-items:center;gap:6px}
.btn-red{display:flex;align-items:center;gap:10px;background:var(--red);color:var(--white);border-radius:22px;font-size:12.5px;font-weight:500;text-transform:uppercase;padding:0 16px 0 6px}
.btn-red .ico{width:26px;height:26px;border-radius:50%;background:var(--white);display:flex;align-items:center;justify-content:center}
.nav{left:0;top:92px;width:1200px;height:38px;background:var(--cyan)}
.nav ul{list-style:none;display:flex;position:absolute;left:142px;top:0;height:38px}
.nav li{height:38px;display:flex;align-items:center;padding:0 20px;font-size:11px;color:var(--white);font-weight:500;text-transform:uppercase;border-right:1px solid rgba(255,255,255,.35)}
.nav li.active{background:var(--red);padding:0 28px}

/* hero */
.hero{left:0;top:130px;width:1200px;height:543px;background:linear-gradient(100deg,#3a3a3a 0%,#6b6b6b 45%,#9a9a9a 70%,#3f3f3f 100%)}
.hero-title{left:142px;top:157px;font-size:34px;line-height:42px;font-weight:500;color:var(--white);text-transform:uppercase}
.hero-title span{color:var(--cyan)}
.hero-sub{left:142px;top:285px;width:400px;font-size:17px;line-height:25px;color:var(--white);font-weight:500}
.hero .btn-red{left:142px;top:356px;height:40px;font-size:14px}

/* treatments */
.tab{background:var(--cyan);color:var(--white);font-family:"Questrial",sans-serif;font-size:26px;letter-spacing:2px;text-transform:uppercase;display:flex;align-items:center;justify-content:center}
.tab span{transform:rotate(-90deg);white-space:nowrap}
.treat{width:230px;text-align:center}
.treat-pic{width:202px;height:202px;border-radius:50%;margin:0 auto;border:2px solid var(--cyan);padding:10px;position:relative}
.treat-pic i{display:block;width:100%;height:100%;border-radius:50%}
.treat-stem{width:1px;height:38px;background:var(--cyan);margin:0 auto}
.treat h3{font-family:"Questrial",sans-serif;font-weight:400;font-size:18px;line-height:20px;color:var(--ink);text-transform:uppercase;margin-top:2px}
.treat p{font-size:12px;line-height:16px;margin-top:10px;padding:0 10px}
.more{color:var(--red);font-size:12.5px;font-weight:500;text-transform:uppercase;display:inline-block;margin-top:8px}

/* feature blocks */
.frame{background:var(--cyan)}
.frame h2{font-family:"Questrial",sans-serif;font-weight:400;font-size:26px;letter-spacing:3px;color:var(--white);text-transform:uppercase;text-align:center;padding-top:20px}
.photo{}
.rule{height:1px;background:var(--cyan)}
.copy{font-size:11.5px;line-height:19px;color:var(--body);text-align:justify}
.copy .lead{font-size:14.5px;line-height:20px;color:var(--ink);font-weight:500;text-align:left;margin-bottom:22px}
.copy .lead b{color:var(--red);font-weight:500}
.copy p+p{margin-top:18px}

/* stretching */
.stretch{width:110px;text-align:center}
.stretch i{display:block;width:62px;height:62px;border-radius:50%;border:1.5px solid #f3b7bd;margin:0 auto}
.stretch.on i{background:var(--red);border-color:var(--red)}
.stretch span{display:block;margin-top:10px;font-size:13px;color:var(--ink)}

/* reviews */
.review-pic{width:202px;height:202px;border-radius:50%;background:var(--cyan);padding:12px}
.review-pic i{display:block;width:100%;height:100%;border-radius:50%;background:linear-gradient(150deg,#9a8c80,#4c566c)}
.quote-mark{font-family:Georgia,serif;font-size:110px;color:#d8d8d8;line-height:1}
.review-text{font-size:13px;line-height:23px;font-style:italic;font-weight:300;color:var(--ink)}
.review-name{font-size:14px;color:var(--red);font-weight:500;margin-top:12px}
.dots{display:flex;flex-direction:column;gap:6px}
.dots i{width:7px;height:7px;border-radius:50%;border:1px solid var(--cyan)}
.dots i.on{background:var(--cyan)}
.gallery{display:flex;gap:15px}
.gallery i{width:141px;height:140px;display:block}

/* location */
.contact{display:flex;align-items:center;gap:18px;font-size:14.5px;color:var(--ink)}
.contact .c-ico{width:38px;height:38px;border-radius:50%;background:var(--red);display:flex;align-items:center;justify-content:center;flex:none}
.contact small{display:block;font-size:11.5px;color:var(--body)}

/* footer */
.footer{left:0;top:4635px;width:1200px;height:378px;background:var(--dark)}
.footer .brand-name{font-size:18px}
.foot-text{left:142px;top:130px;width:360px;font-size:11.5px;line-height:18px;color:#bdbdbd;text-align:justify}
.foot-h{font-family:"Questrial",sans-serif;font-size:17px;color:var(--white);letter-spacing:1px}
.foot-h span{color:var(--cyan)}
.foot-links{list-style:none;font-size:11.5px;color:#d0d0d0;line-height:27px;margin-top:22px}
.foot-links li:first-child{color:var(--cyan)}
.field{border:1px solid #6a6a6a;color:#9a9a9a;font-size:11px;padding:9px 14px;width:263px}
.submit{background:var(--red);color:var(--white);font-size:12px;font-weight:500;text-transform:uppercase;width:108px;height:31px;border-radius:16px;display:flex;align-items:center;justify-content:center}
.copyright{left:0;top:321px;width:1200px;height:57px;background:var(--darker);font-size:11px;color:#bdbdbd;display:flex;align-items:center;justify-content:center}
</style>
</head>
<body>

<header>
  <div class="abs brand" style="left:142px;top:10px">
    <span class="brand-dot"></span>
    <span class="brand-name">Belvan Chiropractic<br>and Sports Therapy</span>
  </div>
  <div class="abs header-phone">
    <svg width="14" height="14" viewBox="0 0 24 24"><path fill="#e8192c" d="M6.6 10.8a15 15 0 0 0 6.6 6.6l2.2-2.2c.3-.3.7-.4 1-.2 1.1.4 2.3.6 3.6.6.6 0 1 .4 1 1V20c0 .6-.4 1-1 1A17 17 0 0 1 3 4c0-.6.4-1 1-1h3.5c.6 0 1 .4 1 1 0 1.3.2 2.5.6 3.6.1.3 0 .7-.2 1z"/></svg>
    555.014.2280
  </div>
  <a class="abs btn-red" style="left:852px;top:27px;height:37px">
    <span class="ico"><svg width="14" height="14" viewBox="0 0 24 24"><path fill="#e8192c" d="M6.6 10.8a15 15 0 0 0 6.6 6.6l2.2-2.2c.3-.3.7-.4 1-.2 1.1.4 2.3.6 3.6.6.6 0 1 .4 1 1V20c0 .6-.4 1-1 1A17 17 0 0 1 3 4c0-.6.4-1 1-1h3.5c.6 0 1 .4 1 1 0 1.3.2 2.5.6 3.6.1.3 0 .7-.2 1z"/></svg></span>
    Book an Appointment
  </a>
  <nav class="abs nav">
    <ul>
      <li class="active">Home</li>
      <li>Location</li>
      <li>Treatments Offered</li>
      <li>New Patient Paperwork</li>
      <li>Stretching</li>
      <li>Social</li>
      <li>Photo Gallery</li>
    </ul>
  </nav>
</header>

<section class="abs hero" role="img" aria-label="Black and white photo of two sprinters racing on a track">
  <h1 class="abs hero-title">We Facilitate Healing<br><span>&amp; Optimum Physical</span><br>Performance</h1>
  <p class="abs hero-sub">By Restoring Balance To The Body – Muscle, Joint &amp; Nerve</p>
  <a class="abs btn-red">
    <span class="ico"><svg width="14" height="14" viewBox="0 0 24 24"><path fill="#e8192c" d="M6.6 10.8a15 15 0 0 0 6.6 6.6l2.2-2.2c.3-.3.7-.4 1-.2 1.1.4 2.3.6 3.6.6.6 0 1 .4 1 1V20c0 .6-.4 1-1 1A17 17 0 0 1 3 4c0-.6.4-1 1-1h3.5c.6 0 1 .4 1 1 0 1.3.2 2.5.6 3.6.1.3 0 .7-.2 1z"/></svg></span>
    Book an Appointment
  </a>
</section>

<!-- treatments -->
<div class="abs tab" style="left:1130px;top:673px;width:70px;height:533px"><span>Treatments Offered</span></div>
<article class="abs treat" style="left:128px;top:760px">
  <div class="treat-pic" style="border-width:0;background:var(--cyan)"><i role="img" aria-label="Photo of the clinic treatment room" style="background:linear-gradient(160deg,#d8d8d8,#6d6d6d)"></i></div>
  <div class="treat-stem"></div>
  <h3>The Belvan<br>Protocol</h3>
  <p>The Belvan Protocol, or TBP, is a comprehensive system of chiropractic...</p>
  <a class="more">Read More »</a>
</article>
<article class="abs treat" style="left:365px;top:760px">
  <div class="treat-pic"><i role="img" aria-label="Photo of hands applying myofascial release" style="background:linear-gradient(150deg,#e8b48a,#9c5a34)"></i></div>
  <div class="treat-stem"></div>
  <h3>Myofascial<br>Release</h3>
  <p>Myofascial therapy is a safe, low force therapy that releases and heals soft tissue restrictions...</p>
  <a class="more">Read More »</a>
</article>
<article class="abs treat" style="left:605px;top:760px">
  <div class="treat-pic"><i role="img" aria-label="Photo of an athlete's muscular back" style="background:linear-gradient(150deg,#c08a6a,#2a1c16)"></i></div>
  <div class="treat-stem"></div>
  <h3>Active Release<br>Therapy</h3>
  <p>Active Release Therapy (ART) is extremely effective in soft tissue treatment. ART is...</p>
  <a class="more">Read More »</a>
</article>
<article class="abs treat" style="left:842px;top:760px">
  <div class="treat-pic"><i role="img" aria-label="Black and white photo of trigger point therapy on a back" style="background:linear-gradient(150deg,#a0a0a0,#1c1c1c)"></i></div>
  <div class="treat-stem"></div>
  <h3>Trigger Point<br>Therapy</h3>
  <p>Trigger point therapy addresses most muscle pains, which can occur at various...</p>
  <a class="more">Read More »</a>
</article>

<!-- mission -->
<div class="abs frame" style="left:185px;top:1206px;width:457px;height:438px"><h2>Mission Statement</h2></div>
<div class="abs photo" role="img" aria-label="Photo of beach volleyball players at the net" style="left:142px;top:1276px;width:457px;height:422px;background:linear-gradient(160deg,#2f6fb0 0%,#d7c63a 45%,#c9a545 70%,#3a5fa0 100%)"></div>
<div class="abs rule" style="left:642px;top:1239px;width:50px"></div>
<div class="abs copy" style="left:714px;top:1236px;width:346px">
  <p class="lead">Our goal at <b>Belvan Chiropractic and Sports Therapy</b> is to facilitate healing and optimum physical performance through a partnership with our patients.</p>
  <p>By restoring balance to the body – muscle, joint and nerve – we provide a starting point where the patient can then take control of their health and well-being. The doctors here provide assessment and instruction on proper posture, exercise biomechanics, nutrition and lifestyle behaviors needed to maintain the health benefits achieved here in our office.</p>
  <p>At Belvan Chiropractic and Sports Therapy we use a proven systematic approach to diagnose and treat musculoskeletal injuries and we call it The Belvan Protocol for soft tissue and joint injury. From professional athletes to grandparents, The Belvan Protocol is profoundly effective in the treatment of athletic injuries, chronic pain and stiffness and many of the functional difficulties normally associated with aging. It can be truly life changing.</p>
</div>

<!-- stretching -->
<div class="abs stretch" style="left:175px;top:1819px"><i></i><span>Hamstring</span></div>
<div class="abs stretch" style="left:345px;top:1819px"><i></i><span>Piriformis</span></div>
<div class="abs stretch on" style="left:175px;top:1930px"><i></i><span>Groin/Adductor</span></div>
<div class="abs stretch" style="left:345px;top:1930px"><i></i><span>Quadricep</span></div>
<div class="abs stretch" style="left:175px;top:2038px"><i></i><span>Hip Flexor</span></div>
<div class="abs stretch" style="left:345px;top:2038px"><i></i><span>Pectoral</span></div>
<div class="abs stretch" style="left:175px;top:2149px"><i></i><span>Calves/Achilles</span></div>
<div class="abs stretch" style="left:345px;top:2149px"><i></i><span>Shin</span></div>
<div class="abs rule" style="left:508px;top:1820px;width:95px"></div>
<div class="abs frame" style="left:558px;top:1784px;width:457px;height:449px"><h2>About Stretching</h2></div>
<div class="abs photo" role="img" aria-label="Photo of a climber stretching across a rock wall" style="left:601px;top:1854px;width:457px;height:422px;background:linear-gradient(150deg,#4a5a3a,#7e6e55 50%,#2e3a30)"></div>

<!-- doctor one -->
<div class="abs frame" style="left:185px;top:2363px;width:457px;height:448px"><h2>Dr. Wes Belvan</h2></div>
<div class="abs photo" role="img" aria-label="Portrait photo of Dr. Wes Belvan" style="left:142px;top:2431px;width:457px;height:424px;background:linear-gradient(160deg,#d4c9b8,#9b8f80 55%,#b7b9c4)"></div>
<div class="abs rule" style="left:594px;top:2398px;width:98px"></div>
<div class="abs copy" style="left:714px;top:2392px;width:346px">
  <p class="lead"><b>Dr. Wes Belvan</b> is the owner &amp; clinic director for Belvan Chiropractic and Sports Therapy.</p>
  <p>He is a native Texan, growing up in the Dallas area and attended Northfield State University on a basketball scholarship. Upon finishing his academic and basketball career at NSU, Dr. Belvan traveled and worked throughout Europe for 3 years before discovering beach volleyball and relocating to Miami Beach, FL. It was while competing on the East Coast pro-beach volleyball circuit that he experienced the awesome power of chiropractic and physical medicine. The injuries and chronic conditions that are a part of playing competitive sports had become debilitating for Dr. Belvan at a time when he should have been at peak physical condition and performance. Through a combination of chiropractic treatment, physical medicine and soft-tissue therapy, Dr. Belvan was able to resume playing the sport he loved pain free and stronger than ever.</p>
  <a class="more" style="margin-top:22px">Read More »</a>
</div>

<!-- doctor two -->
<div class="abs copy" style="left:142px;top:2968px;width:344px">
  <p class="lead"><b>Dr. Tara Holloway</b> attended chiropractic school at Harmon University in Dallas, TX, &amp; is originally from Linwood, OK.</p>
  <p>She started her career in healthcare there as a licensed massage therapist, but quickly decided that her clients needed more than what massage could offer. "How could I release muscle tissue but not address the joint dysfunction?" "What would be the best way to make profound, life-long changes in peoples' lives?", she asked herself. In her quest to answer these questions, Dr. Holloway found chiropractic and her true passion.</p>
  <p>Since graduating from Harmon University, Dr. Holloway has sought to integrate soft tissue therapy, chiropractic and multiple modalities into her professional philosophy, always seeking "new and better ways to get people better!" Upon meeting Dr. Belvan, she knew she had found her mentor and has continued to evolve and thrive under his tutelage.</p>
  <a class="more" style="margin-top:22px">Read More »</a>
</div>
<div class="abs rule" style="left:508px;top:2978px;width:95px"></div>
<div class="abs frame" style="left:558px;top:2943px;width:457px;height:445px"><h2>Dr. Tara Holloway</h2></div>
<div class="abs photo" role="img" aria-label="Portrait photo of Dr. Tara Holloway" style="left:601px;top:3011px;width:457px;height:422px;background:linear-gradient(160deg,#cfc9c2,#8a5a3a 50%,#e9e6e2)"></div>

<!-- reviews -->
<div class="abs tab" style="left:0;top:3454px;width:70px;height:374px"><span>Patient's Reviews</span></div>
<div class="abs review-pic" style="left:142px;top:3519px"><i role="img" aria-label="Photo of a smiling patient"></i></div>
<div class="abs quote-mark" style="left:390px;top:3585px">“</div>
<div class="abs" style="left:486px;top:3538px;width:530px">
  <p class="review-text">Lorem ipsum dolor sit amet, consectetuer adipiscing elit, sed diam ok nonummy nibh euismod tincidunt ut laoreet dolore magna aliquam erat volutpat. Ut o wisi enim ad minim veniam, quis nostrud exerci tation ullamcorper suscipitml lobortis nisl ut aliquip ex ea commodo consequat. Duis autem vel eum iriure dolor in mor hendrerit in vulputate velit esse molestie consequat.</p>
  <p class="review-name">- Mrs. Lena Marsh</p>
</div>
<div class="abs dots" style="left:1049px;top:3575px"><i class="on"></i><i></i><i></i><i></i><i></i><i></i></div>

<!-- gallery -->
<div class="abs gallery" style="left:142px;top:3828px">
  <i role="img" aria-label="Photo of a person meditating at sunset" style="background:linear-gradient(180deg,#c79a74,#4a3a30)"></i>
  <i role="img" aria-label="Photo of a tennis racket on a clay court" style="background:linear-gradient(160deg,#d0622e,#a84420)"></i>
  <i role="img" aria-label="Photo of a salad and a measuring tape" style="background:linear-gradient(160deg,#f1f1ee,#6e9a3a)"></i>
  <i role="img" aria-label="Photo of a family walking on the beach" style="background:linear-gradient(180deg,#b8cde0,#c8b894)"></i>
  <i role="img" aria-label="Photo of a rack of dumbbells" style="background:linear-gradient(160deg,#6a6a6a,#1a1a1a)"></i>
  <i role="img" aria-label="Aerial photo of a baseball field" style="background:linear-gradient(160deg,#2f6a40,#a06a44)"></i>
</div>
<div class="abs tab" style="left:1130px;top:3828px;width:70px;height:227px"><span>Social</span></div>

<!-- location -->
<div class="abs frame" style="left:185px;top:4055px;width:457px;height:448px"><h2>Our Location</h2></div>
<div class="abs" role="img" aria-label="Street map showing the clinic location" style="left:142px;top:4127px;width:457px;height:420px;background:linear-gradient(150deg,#eef0f2,#dfe6ec 50%,#e9ecdf)"></div>
<div class="abs rule" style="left:594px;top:4092px;width:98px"></div>
<div class="abs contact" style="left:714px;top:4092px">
  <span class="c-ico"><svg width="16" height="18" viewBox="0 0 24 24"><path fill="#fff" d="M12 2a7 7 0 0 0-7 7c0 5 7 13 7 13s7-8 7-13a7 7 0 0 0-7-7zm0 9.5A2.5 2.5 0 1 1 12 6.5a2.5 2.5 0 0 1 0 5z"/></svg></span>
  <span>Belvan Chiropractic + Sports Therapy<small>418 Meridian Way, Oakfield, TX 75990</small></span>
</div>
<div class="abs contact" style="left:714px;top:4153px">
  <span class="c-ico"><svg width="16" height="16" viewBox="0 0 24 24"><path fill="#fff" d="M6.6 10.8a15 15 0 0 0 6.6 6.6l2.2-2.2c.3-.3.7-.4 1-.2 1.1.4 2.3.6 3.6.6.6 0 1 .4 1 1V20c0 .6-.4 1-1 1A17 17 0 0 1 3 4c0-.6.4-1 1-1h3.5c.6 0 1 .4 1 1 0 1.3.2 2.5.6 3.6.1.3 0 .7-.2 1z"/></svg></span>
  <span>555.014.2280</span>
</div>
<div class="abs contact" style="left:714px;top:4217px">
  <span class="c-ico"><svg width="16" height="16" viewBox="0 0 24 24"><path fill="#fff" d="M7 3h10v5H7zM4 9h16a1 1 0 0 1 1 1v7h-4v4H7v-4H3v-7a1 1 0 0 1 1-1zm5 7v3h6v-3z"/></svg></span>
  <span>555.014.2281</span>
</div>
<div class="abs contact" style="left:714px;top:4281px">
  <span class="c-ico"><svg width="16" height="14" viewBox="0 0 24 20"><path fill="#fff" d="M2 2h20v16H2zm2 2v.5l8 5.5 8-5.5V4z"/></svg></span>
  <span style="font-size:13px">info@belvanspinefit.com</span>
</div>

<!-- footer -->
<footer class="abs footer">
  <div class="abs brand" style="left:142px;top:62px">
    <span class="brand-dot"></span>
    <span class="brand-name">Belvan Chiropractic<br>and Sports Therapy</span>
  </div>
  <p class="abs foot-text">At Belvan Chiropractic and Sports Therapy we use a proven systematic approach to diagnose and treat musculoskeletal injuries and we call it The Belvan Protocol for soft tissue and joint injury. From professional athletes to grandparents, The Belvan Protocol is profoundly effective in the treatment of athletic injuries, chronic pain and stiffness and many of the functional difficulties normally associated with aging. It can be truly life changing.<br><a class="more" style="font-size:11px;margin-top:6px">Read More »</a></p>
  <div class="abs" style="left:589px;top:62px">
    <h4 class="foot-h" style="font-weight:400">Quick <span>Links</span></h4>
    <ul class="foot-links">
      <li>Home</li><li>Location</li><li>Treatments Offered</li><li>New Patient Paperwork</li><li>Stretching</li><li>Social</li><li>Photo Gallery</li>
    </ul>
  </div>
  <div class="abs" style="left:797px;top:62px">
    <h4 class="foot-h" style="font-weight:400">Quick <span>Inquiry</span></h4>
    <div class="field" style="margin-top:22px;height:32px">Name</div>
    <div class="field" style="margin-top:7px;height:32px">Email</div>
    <div class="field" style="margin-top:7px;height:46px">Message</div>
    <div class="submit" style="margin-top:16px">Submit</div>
  </div>
  <div class="abs copyright">Copyright © 2019 BELVAN. All Rights Reserved.</div>
</footer>

</body>
</html>
```